Brevant Composite Decking

We need a vast amount of work doing on a new product launch for our composite decking products. We will have seven new systems coming online in the next four months time so we require a person to work with us throughout this time. We will also require package boxes and designs created too.Currently we have one range of product. This decking system is called our Meridale Range. Brevant Polymer Works LLC are the manufacturers of the decking and our brand is called Brevant Decking. Our composite decking is a wood and PVC mix board that is used for outdoors.
I have attached some brochures that I had my friend do for to launch of our Meridale range of product. This will give you some idea on what we do. We now need to get everything done properly moving forward. You can get more information on our company at www.brevantpolymers.example
Please let me know if you require any additional information on the products.
Kind regards,

Tomas Verhelm

Target Market(s)

Business to Business and Retail Customer

Industry/Entity Type

It Company

Requirements
Must have
• Keep our Brevant Decking word.

```html
<!DOCTYPE html>
<html lang="en">
<head>
<meta charset="utf-8">
<title>Brevant Decking – Composite Decking, Meridale Range</title>
<link href="https://fonts.googleapis.com/css2?family=Fira+Sans+Condensed:wght@300;400;500&family=Fira+Sans:wght@300;400;500&display=swap" rel="stylesheet">
<style>
  :root {
    --charcoal: #3c3c3c;
    --charcoal-dark: #333333;
    --taupe: #aca596;
    --taupe-light: #b9b3a6;
    --taupe-dark: #9c9586;
    --white: #ffffff;
    --nav-text: #b8b8b8;
    --nav-active: #e4e4e4;
  }
  * { box-sizing: border-box; margin: 0; padding: 0; }
  html, body { width: 1200px; height: 848px; overflow: hidden; background: var(--charcoal); }
  .cover {
    position: relative; width: 1200px; height: 848px; overflow: hidden;
    background: var(--charcoal);
    font-family: "Fira Sans", Arial, sans-serif;
  }
  .header-band { position: absolute; left: 0; top: 0; width: 1200px; height: 193px; background: var(--charcoal); }
  .brand {
    position: absolute; right: 72px; top: 62px;
    display: flex; align-items: center; gap: 16px;
    color: var(--white); font-family: "Fira Sans", Arial, sans-serif;
    font-weight: 400; font-size: 46px; letter-spacing: 0.5px;
  }
  .brand-mark { width: 22px; height: 22px; border-radius: 50%; background: var(--white); }
  .body-panel {
    position: absolute; left: 0; top: 193px; width: 1200px; height: 607px;
    background: var(--taupe);
  }
  .content-sheet {
    position: absolute; left: 0; top: 193px; width: 1140px; height: 607px;
    background: linear-gradient(180deg, var(--taupe-light) 0%, var(--taupe) 60%, var(--taupe-dark) 100%);
    box-shadow: 4px 0 8px rgba(0,0,0,0.25);
  }
  .gallery { position: absolute; top: 205px; left: 0; height: 272px; }
  .photo { position: absolute; top: 0; height: 272px; }
  .photo-pool-deck { left: 0; width: 285px; background: linear-gradient(160deg, #4f6b3c 0%, #7a4030 45%, #8c4532 100%); }
  .photo-terrace { left: 293px; width: 274px; background: linear-gradient(170deg, #6f7a6a 0%, #7d6858 40%, #8a735f 100%); }
  .photo-pool-modern { left: 578px; width: 273px; background: linear-gradient(170deg, #8fa0a8 0%, #5f8a3f 35%, #a7a49f 70%, #b9b6b0 100%); }
  .photo-garden { left: 862px; width: 275px; background: linear-gradient(170deg, #4d7a3a 0%, #8d5b52 30%, #d2cfc2 65%, #e0ddd2 100%); }
  .range-badge {
    position: absolute; left: 71px; top: 120px; width: 140px; height: 140px;
    border-radius: 50%; background: #8d8578; border: 4px solid #d8d3c8;
  }
  .title-block { position: absolute; right: 125px; top: 530px; text-align: right; color: var(--white); }
  .title {
    font-family: "Fira Sans Condensed", Arial, sans-serif;
    font-size: 46px; letter-spacing: 2px; line-height: 1; font-weight: 300;
  }
  .title strong { font-weight: 500; }
  .title-rule { width: 407px; margin: 16px 0 0 auto; border-top: 2px dotted rgba(255,255,255,0.85); }
  .subtitle {
    margin-top: 12px; font-family: "Fira Sans Condensed", Arial, sans-serif;
    font-size: 30px; font-weight: 300; line-height: 1;
  }
  .subtitle strong { font-weight: 500; }
  .footer-band {
    position: absolute; left: 0; top: 800px; width: 1200px; height: 48px;
    background: var(--charcoal-dark);
  }
  .divisions {
    position: absolute; left: 52px; top: 816px; list-style: none; display: flex;
    font-family: "Fira Sans Condensed", Arial, sans-serif; font-size: 12.5px;
    color: var(--nav-text); letter-spacing: 0.4px;
  }
  .divisions li + li::before { content: "|"; margin: 0 7px; }
  .divisions .active { color: var(--nav-active); font-weight: 500; }
  .site-url {
    position: absolute; right: 123px; top: 815px;
    font-family: "Fira Sans Condensed", Arial, sans-serif; font-size: 13px; color: var(--white);
  }
</style>
</head>
<body>
<main class="cover">
  <div class="header-band"></div>
  <div class="brand"><span class="brand-mark"></span><span>Brevant Decking</span></div>

  <div class="body-panel"></div>
  <div class="content-sheet"></div>

  <div class="gallery">
    <div class="photo photo-pool-deck" role="img" aria-label="Red-brown composite deck beside a pool and hot tub with patio furniture"></div>
    <div class="photo photo-terrace" role="img" aria-label="Brown composite terrace with steps and outdoor lounge seating"></div>
    <div class="photo photo-pool-modern" role="img" aria-label="Pale grey composite deck around a modern pool with lawn and mountains"></div>
    <div class="photo photo-garden" role="img" aria-label="Light composite deck with railing in a garden"></div>
  </div>

  <div class="range-badge" aria-hidden="true"></div>

  <div class="title-block">
    <h1 class="title"><strong>COMPOSITE</strong> DECKING</h1>
    <div class="title-rule"></div>
    <p class="subtitle"><strong>Meridale</strong> Range</p>
  </div>

  <footer class="footer-band"></footer>
  <ul class="divisions">
    <li class="active">DECKING</li>
    <li>FENCING</li>
    <li>PLASTICS</li>
    <li>SIGNAGE</li>
    <li>CONTRACTING</li>
    <li>ELECTRICAL WASTE</li>
    <li>MODULAR BUILDINGS</li>
  </ul>
  <p class="site-url">www.brevantdecking.example</p>
</main>
</body>
</html>
```